New Business Card Design Project

We want a modern business card that catches the attention of other remodeling companies as well as homeowners. We would like it to be informative but still simple.

Target Market(s)

Residential and other Business's

Contact Information for Business Card

TidyKraft
Phone number is 5152947718
Address is
4817 SW 3rd Lane
Des Moines, Iowa 50313
email is tidykraftia@mailorbit.net

Requirements
Must have
• Our tagline
• Honest | Professional | Affordable

```html
<!DOCTYPE html>
<html lang="en">
<head>
<meta charset="utf-8">
<title>TidyKraft Business Card</title>
<link rel="stylesheet" href="https://fonts.googleapis.com/css2?family=Oswald:wght@600&family=Roboto:wght@400;500;700;900&display=swap">
<style>
  :root {
    --backdrop: #3b3b3d;
    --card-dark: #242426;
    --brand-blue: #1a6ad6;
    --brand-orange: #e3600f;
    --text-light: #ffffff;
    --text-dark: #0e2a55;
  }
  * { box-sizing: border-box; margin: 0; padding: 0; }
  html, body { width: 799px; height: 1200px; overflow: hidden; }
  body {
    background: var(--backdrop);
    font-family: "Roboto", Arial, sans-serif;
    position: relative;
  }
  .card {
    position: absolute;
    left: 60px;
    width: 680px;
    height: 389px;
    background: var(--card-dark);
    border-radius: 6px;
    overflow: hidden;
    box-shadow: 0 14px 30px rgba(0,0,0,.45);
  }
  .card--front { top: 150px; }
  .card--back { top: 670px; }

  .brand-name {
    font-family: "Roboto", Arial, sans-serif;
    font-weight: 900;
    color: var(--brand-blue);
    letter-spacing: 1px;
    line-height: 1;
  }
  .tagline {
    font-family: "Oswald", "Arial Narrow", sans-serif;
    font-weight: 600;
    color: var(--brand-blue);
    text-transform: uppercase;
    letter-spacing: 1px;
  }

  /* Front */
  .front-lockup {
    position: absolute;
    top: 105px; left: 0; right: 0;
    text-align: center;
  }
  .front-lockup .brand-name { font-size: 84px; }
  .front-lockup .tagline { font-size: 25px; margin-top: 10px; }
  .front-web {
    position: absolute;
    top: 300px; left: 0; right: 0;
    display: flex; justify-content: center; align-items: center; gap: 40px;
    color: var(--text-light);
    font-size: 19px;
  }
  .front-web .rule { width: 36px; height: 3px; background: var(--brand-orange); }

  /* Back */
  .back-waves { position: absolute; inset: 0; }
  .back-lockup { position: absolute; top: 26px; left: 48px; }
  .back-lockup .brand-name { font-size: 60px; }
  .back-lockup .tagline { font-size: 18px; margin-top: 6px; }
  .back-address {
    position: absolute; left: 40px; top: 262px;
    color: var(--text-light); font-size: 16px; line-height: 1.45;
  }
  .back-person {
    position: absolute; right: 40px; top: 250px; text-align: right;
    color: var(--text-light);
  }
  .back-person .person-name { font-size: 24px; font-weight: 700; }
  .back-person .person-role { font-size: 16px; margin-top: 2px; }
  .contact-list {
    position: absolute; right: 40px; top: 308px; list-style: none;
    color: var(--text-light); font-size: 16px; line-height: 1.4;
  }
  .contact-list li { display: flex; justify-content: flex-end; align-items: center; gap: 12px; }
  .contact-list svg { width: 15px; height: 15px; fill: var(--text-light); }
</style>
</head>
<body>
  <section class="card card--front">
    <div class="front-lockup">
      <div class="brand-name">TidyKraft</div>
      <div class="tagline">Honest | Professional | Affordable</div>
    </div>
    <div class="front-web">
      <span class="rule"></span>
      <span>www.tidykraft.com</span>
      <span class="rule"></span>
    </div>
  </section>

  <section class="card card--back">
    <svg class="back-waves" viewBox="0 0 680 389" preserveAspectRatio="none" aria-hidden="true">
      <path d="M0,150 C210,120 400,240 680,160 L680,182 C400,262 210,150 0,172 Z" fill="var(--brand-orange)"/>
      <path d="M0,192 C200,170 390,290 680,200 L680,389 L0,389 Z" fill="var(--brand-blue)"/>
    </svg>
    <div class="back-lockup">
      <div class="brand-name">TidyKraft</div>
      <div class="tagline">Honest | Professional | Affordable</div>
    </div>
    <div class="back-address">
      4817 SW 3rd Lane<br>Des Moines, Iowa 50313
    </div>
    <div class="back-person">
      <div class="person-name">Dale Morgan Reyes</div>
      <div class="person-role">Managing Director</div>
    </div>
    <ul class="contact-list">
      <li>5152947718
        <svg viewBox="0 0 16 16"><path d="M3 1l3 3-1.5 2a9 9 0 0 0 5.5 5.5L12 10l3 3-2 2C7 15 1 9 1 3z"/></svg></li>
      <li>tidykraftia@mailorbit.net
        <svg viewBox="0 0 16 16"><path d="M1 3h14v10H1z M1 3l7 6 7-6" fill="none" stroke="#fff" stroke-width="1.6"/></svg></li>
      <li>www.tidykraft.com
        <svg viewBox="0 0 16 16"><circle cx="8" cy="8" r="6.5" fill="none" stroke="#fff" stroke-width="1.4"/><path d="M1.5 8h13M8 1.5c-3 3.5-3 9.5 0 13M8 1.5c3 3.5 3 9.5 0 13" fill="none" stroke="#fff" stroke-width="1.2"/></svg></li>
    </ul>
  </section>
</body>
</html>
```